Business Card Design Project

I need a business card design for our new logo, please check the logo at the following link:
https://files.quorvane-share.com/s/p7tkwe3nq4zr81h/FernCove.png
The address on the business card:
Av. Olegário Tavares 418 sala 207
Barra da Tijuca, Rio de Janeiro, RJ
CEP: 24917-380
Brasil
Phone: +55 21 73408216
e-mail: rogerio@ferncove-exemplo.com.br
Updates
Thank you all for sending your designs, we will not provide feedback because there are too many designs, on December 3 we will pick the best design according to our point of view. Please keep posting.
Rogério
Industry/Entity Type
Business

```html
<!DOCTYPE html>
<html lang="pt-BR">
<head>
<meta charset="UTF-8">
<title>FernCove – Cartão de visita</title>
<link rel="stylesheet" href="https://fonts.googleapis.com/css2?family=Open+Sans:wght@400;600;700&family=Crimson+Text:wght@400&display=swap">
<style>
  :root {
    --backdrop: #e9e7e3;
    --card-white: #ffffff;
    --card-black: #1c1c1c;
    --accent-yellow: #f2c21b;
    --text-dark: #1e1e1e;
    --text-muted: #9a9a9a;
  }
  * { margin: 0; padding: 0; box-sizing: border-box; }
  html, body {
    width: 1200px;
    height: 900px;
    overflow: hidden;
    background: var(--backdrop);
  }
  .canvas {
    position: relative;
    width: 1200px;
    height: 900px;
  }
  .card {
    position: absolute;
    left: 320px;
    width: 560px;
    height: 320px;
    background: var(--card-white);
    box-shadow: 0 6px 18px rgba(0,0,0,0.18);
    overflow: hidden;
  }
  .card--front { top: 100px; }
  .card--back { top: 480px; }
  .card__shape {
    position: absolute;
    inset: 0;
    width: 560px;
    height: 320px;
  }
  .shape-dark { fill: var(--card-black); }
  .shape-edge { fill: none; stroke: var(--accent-yellow); stroke-width: 3; }

  .brand {
    position: absolute;
    display: flex;
    align-items: center;
    gap: 10px;
  }
  .brand__dot {
    width: 22px;
    height: 22px;
    border-radius: 50%;
    background: var(--accent-yellow);
  }
  .brand__name {
    font-family: "Open Sans", sans-serif;
    font-weight: 700;
    font-size: 34px;
    color: var(--text-dark);
    letter-spacing: -0.5px;
  }
  .card--front .brand { left: 330px; top: 195px; }
  .brand__web {
    position: absolute;
    left: 364px;
    top: 244px;
    font-family: "Open Sans", sans-serif;
    font-weight: 600;
    font-size: 13px;
    color: var(--text-dark);
  }
  .card--back .brand { left: 52px; top: 150px; }

  .contact {
    position: absolute;
    right: 30px;
    top: 78px;
    text-align: right;
    color: var(--accent-yellow);
  }
  .contact__name {
    font-family: "Open Sans", sans-serif;
    font-weight: 600;
    font-size: 20px;
  }
  .contact__role {
    font-family: "Open Sans", sans-serif;
    font-size: 10px;
    color: var(--text-muted);
    margin-bottom: 26px;
  }
  .contact__line {
    font-family: "Crimson Text", serif;
    font-size: 13px;
    line-height: 1.35;
  }
  .contact__line--gap { margin-bottom: 14px; }
  .icon {
    display: inline-block;
    width: 11px;
    height: 11px;
    margin-right: 5px;
    vertical-align: -1px;
    fill: var(--accent-yellow);
  }
</style>
</head>
<body>
<main class="canvas">

  <section class="card card--front" aria-label="Frente do cartão">
    <svg class="card__shape" viewBox="0 0 560 320" aria-hidden="true">
      <path class="shape-dark" d="M0,0 H430 C350,50 320,160 220,205 C150,236 70,245 0,245 Z"/>
      <path class="shape-edge" d="M430,0 C350,50 320,160 220,205 C150,236 70,245 0,245"/>
    </svg>
    <div class="brand">
      <span class="brand__dot"></span>
      <span class="brand__name">FernCove</span>
    </div>
    <p class="brand__web">www.ferncove.com.br</p>
  </section>

  <section class="card card--back" aria-label="Verso do cartão">
    <svg class="card__shape" viewBox="0 0 560 320" aria-hidden="true">
      <path class="shape-dark" d="M80,320 C150,285 210,255 250,175 C295,85 380,35 560,25 V320 Z"/>
      <path class="shape-edge" d="M80,320 C150,285 210,255 250,175 C295,85 380,35 560,25"/>
    </svg>
    <div class="brand">
      <span class="brand__dot"></span>
      <span class="brand__name">FernCove</span>
    </div>
    <div class="contact">
      <p class="contact__name">Rogério Rogério</p>
      <p class="contact__role">Owner</p>
      <p class="contact__line contact__line--gap">
        <svg class="icon" viewBox="0 0 24 24" aria-hidden="true"><path d="M6.6 10.8a15.1 15.1 0 0 0 6.6 6.6l2.2-2.2a1 1 0 0 1 1-.25 11.4 11.4 0 0 0 3.6.57 1 1 0 0 1 1 1V20a1 1 0 0 1-1 1A17 17 0 0 1 3 4a1 1 0 0 1 1-1h3.5a1 1 0 0 1 1 1c0 1.25.2 2.45.57 3.57a1 1 0 0 1-.25 1z"/></svg>+55 21 73408216
      </p>
      <p class="contact__line">
        <svg class="icon" viewBox="0 0 24 24" aria-hidden="true"><path d="M2 5h20v14H2z M2 5l10 8 10-8" /></svg>rogerio@ferncove-exemplo.com.br
      </p>
      <p class="contact__line">
        <svg class="icon" viewBox="0 0 24 24" aria-hidden="true"><path d="M12 3 2 12h3v9h5v-6h4v6h5v-9h3z"/></svg>Av. Olegário Tavares 418 sala 207
      </p>
      <p class="contact__line">Barra da Tijuca, Rio de Janeiro,</p>
      <p class="contact__line">RJ CEP: 24917-380 &nbsp;Brasil</p>
    </div>
  </section>

</main>
</body>
</html>
```